Power Point Presentation or Canva Slides

Project: Photography Brochure (10-12 pages, A4 size)

Objective: To create a clean, high-end, and easy-to-read PDF brochure showcasing headshot packages for corporate clients, emphasizing value, quality, and a stress-free process.

Project content, logos, brand colours and images can be found here: https://files.brovelmask.net/open?id=7QpLr29XwKtBnVe4sHjM0aYcUd8fGzTiN&usp=share_fx

Design Direction
* Overall Style: Minimal, sophisticated, and modern.
* Use plenty of whitespace to create a breathable layout.

* Professional yet approachable tone.

* High-end look to convey quality and professionalism.

* Ensure text is easy to skim with clear headlines, subheadings, and icons where applicable.

Key Focus Areas:
* Emphasize value the client receives (not just prices).
* Ease of process and genuine expressions are key selling points.
* Testimonials should be scattered throughout as visual callouts, not in blocks.
* Make sure every page looks visually appealing with an appropriate balance of text and images.

Target Market(s)

Businesses - business owners, marketing managers, executive assistants, 50% male and 50% female

Industry/Entity Type

Commercial photography

Font styles to use
Other font styles liked:
• Helvetica

Requirements
Must have
• Minimal, high-end aesthetic (clear, polished, easy to skim), Consistent typography, spacing, and alignment for a professional look Strong emphasis on value for the client (not just listing features), Breathing room in the layout (not text-heavy or overwhelming), Brand consistency (uses provided colors, fonts, and logos correctly)
Nice to have
• A mix of text + visuals for an engaging layout
Should not have
• generic stock feature images (use the supplied images - stock images are OK ONLY if blurred and used as a background with overlay), ), Overcrowded or cluttered pages, Generic, overused Canva templates that feel cheap, Excessive colors or flashy design elements that distract from the message

```html
<!DOCTYPE html>
<html lang="en">
<head>
<meta charset="utf-8">
<title>Marcus Ellery Photography – Corporate Headshot Brochure</title>
<link rel="stylesheet" href="https://fonts.googleapis.com/css2?family=Oswald:wght@300;400;500;600;700&family=Caveat:wght@500&display=swap">
<style>
  :root{
    --stage:#a9a9a9;
    --paper:#ffffff;
    --teal:#27b7c8;
    --green:#52be8e;
    --mint:#d9f2ee;
    --ink:#1d1d1d;
    --muted:#666666;
    --grey-quote:#cfcfcf;
    --star:#f2b01e;
    --figure-top:#2a2a2a;
    --figure-mid:#232323;
    --figure-low:#2f4b6e;
  }
  *{margin:0;padding:0;box-sizing:border-box}
  html,body{width:1200px;height:2252px;overflow:hidden}
  body{background:var(--stage);position:relative;font-family:"Oswald",sans-serif;color:var(--ink)}
  .page{position:absolute;left:235px;width:730px;background:var(--paper);overflow:hidden}
  .page--cover{top:75px;height:1032px}
  .page--intro{top:1141px;height:1034px}
  .page svg.backdrop{position:absolute;inset:0;width:100%;height:100%}
  .abs{position:absolute}

  /* Cover */
  .brand{left:55px;top:44px;width:205px;font-family:"Oswald",sans-serif;font-weight:300;color:var(--ink)}
  .brand__line{display:block;font-size:50px;line-height:1;letter-spacing:2px}
  .brand__tag{display:block;font-size:14px;line-height:1;letter-spacing:6px;text-align:right;margin-top:8px}
  .cover-title{left:52px;top:662px;color:#fff;line-height:1;font-weight:400}
  .cover-title__a{display:block;font-weight:300;font-size:84px;letter-spacing:-1px;line-height:84px}
  .cover-title__b{display:block;font-weight:400;font-size:40px;line-height:42px;margin-top:2px}
  .cover-title__c{display:block;font-weight:700;font-size:57px;line-height:62px;margin-top:2px}
  .cover-lead{left:52px;top:868px;width:400px;color:#fff;font-weight:300;font-size:15.5px;line-height:1.35}
  .cover-note{left:52px;top:930px;color:#fff;font-weight:500;font-style:italic;font-size:16px}

  /* Intro page */
  .hero-figure{left:43px;top:27px;width:268px;height:657px;border-radius:120px 120px 40px 40px;
    background:linear-gradient(180deg,var(--figure-top) 0%,var(--figure-mid) 45%,var(--figure-low) 70%,#26364f 100%)}
  .pain{left:326px;top:40px;width:390px;color:#fff}
  .pain__head{font-weight:600;font-style:italic;font-size:42px;line-height:48px}
  .pain__text{font-weight:300;font-size:15.5px;line-height:1.35;margin-top:22px}
  .pain__text + .pain__text{margin-top:18px}
  .pain__sign{font-family:"Caveat",cursive;font-size:30px;margin-top:10px;line-height:1}
  .pain__role{font-weight:300;font-size:16px}
  .trust{left:326px;top:440px;width:390px;color:#fff}
  .trust__head{font-weight:600;font-style:italic;font-size:40px;line-height:1.2}
  .trust__list{list-style:none;margin-top:14px;font-weight:300;font-size:15.5px;line-height:1.35}
  .trust__list li{padding-left:24px;position:relative}
  .trust__list li::before{content:"·";position:absolute;left:4px}
  .trust__list strong{font-weight:500}
  .quote-mark{font-family:Georgia,serif;font-weight:700;color:var(--grey-quote);font-size:150px;line-height:1}
  .quote-mark--open{left:172px;top:680px}
  .quote-mark--close{left:620px;top:805px}
  .avatar{left:40px;top:752px;width:135px;height:135px;border-radius:50%;border:3px solid var(--teal);
    background:radial-gradient(circle at 50% 40%,#c9a58c 0 28%,#2b2f3a 29% 100%)}
  .testimonial{left:261px;top:752px;width:450px;font-weight:300;font-size:15.5px;line-height:1.35;color:var(--ink)}
  .testimonial__sign{font-family:"Caveat",cursive;font-size:30px;margin-top:8px;line-height:1}
  .testimonial__org{font-size:15.5px;font-weight:300}
  .client{position:absolute;top:950px;transform:translateX(-50%);display:flex;align-items:center;gap:7px;
    font-weight:500;font-size:17px;line-height:24px;color:var(--ink);white-space:nowrap}
  .client__dot{width:14px;height:14px;border-radius:50%;background:var(--ink)}
  .review{left:531px;top:940px;width:180px;font-weight:300;color:var(--ink);line-height:1.2}
  .review__name{font-size:13px}
  .review__addr{font-size:8px;color:var(--muted)}
  .review__score{font-size:13px;margin-top:4px}
  .review__stars{color:var(--star);letter-spacing:1px}
  .review__count{font-size:8px;color:var(--muted)}
</style>
</head>
<body>

<section class="page page--cover">
  <svg class="backdrop" viewBox="0 0 730 1032" aria-hidden="true">
    <defs>
      <linearGradient id="coverSweep" x1="0" y1="0" x2="1" y2="1">
        <stop offset="0" stop-color="#4fbf8e"/>
        <stop offset=".6" stop-color="#2cb7c2"/>
        <stop offset="1" stop-color="#27b7c8"/>
      </linearGradient>
    </defs>
    <circle cx="390" cy="880" r="500" fill="var(--teal)"/>
    <circle cx="300" cy="800" r="410" fill="url(#coverSweep)"/>
    <circle cx="142" cy="254" r="14" fill="var(--mint)"/>
    <circle cx="90" cy="322" r="38" fill="var(--mint)"/>
    <circle cx="712" cy="771" r="38" fill="var(--mint)"/>
    <circle cx="650" cy="969" r="14" fill="var(--mint)"/>
  </svg>

  <svg class="abs" style="left:228px;top:100px" width="512" height="512" viewBox="0 0 512 512" role="img" aria-label="Photographer smiling behind a camera on a tripod, framed in a teal circle">
    <defs>
      <linearGradient id="portraitTone" x1="0" y1="0" x2="1" y2="1">
        <stop offset="0" stop-color="#2cb7c4"/>
        <stop offset=".55" stop-color="#3fbba6"/>
        <stop offset="1" stop-color="#1e2a2c"/>
      </linearGradient>
    </defs>
    <circle cx="256" cy="256" r="256" fill="url(#portraitTone)"/>
  </svg>

  <div class="abs brand">
    <span class="brand__line">MARCUS</span>
    <span class="brand__line">ELLERY</span>
    <span class="brand__tag">PHOTOGRAPHY</span>
  </div>

  <h1 class="abs cover-title">
    <span class="cover-title__a">CORPORATE</span>
    <span class="cover-title__b">HEADSHOT &amp; BRANDING</span>
    <span class="cover-title__c">PHOTOGRAPHY</span>
  </h1>
  <p class="abs cover-lead">Professional, approachable, consistent headshots for your team<br>—no awkward or stiff poses</p>
  <p class="abs cover-note">Easy relaxed process – even if you hate photos</p>
</section>

<section class="page page--intro">
  <svg class="backdrop" viewBox="0 0 730 1034" aria-hidden="true">
    <path d="M0,285 C88,550 375,706 730,731 L730,225 L0,225 Z" fill="var(--green)"/>
    <path d="M0,0 H730 V238 Q266,598 0,165 Z" fill="var(--teal)"/>
    <path d="M0,165 Q266,598 730,238" fill="none" stroke="#fff" stroke-width="7"/>
  </svg>

  <div class="abs hero-figure" role="img" aria-label="Full-length cut-out of the studio owner in a black polo and jeans, holding a camera"></div>

  <div class="abs pain">
    <h2 class="pain__head">Outdated, low-quality,<br>or awkward headshots?</h2>
    <p class="pain__text">A bad photo sends the wrong message about your company.</p>
    <p class="pain__text">My team and I work with companies to deliver professional,<br>consistent, and natural-looking headshots every time—without<br>the awkwardness. Let's make your team look amazing!</p>
    <p class="pain__sign">Marcus Ellery</p>
    <p class="pain__role">Studio Owner</p>
  </div>

  <div class="abs trust">
    <h2 class="trust__head">WHY 500+<br>COMPANIES TRUST US</h2>
    <ul class="trust__list">
      <li><strong>Genuine Expressions</strong>—No awkward photos here</li>
      <li>Easy, Comfortable Process – even if you hate photos</li>
      <li><strong>Consistency</strong> —consistent professional results</li>
      <li>Mobile studio—save time &amp; hassle of studio shoots</li>
    </ul>
  </div>

  <span class="abs quote-mark quote-mark--open">“</span>
  <span class="abs quote-mark quote-mark--close">”</span>

  <div class="abs avatar" role="img" aria-label="Round portrait of the client giving the testimonial"></div>

  <blockquote class="abs testimonial">
    <p>The thought of having a professional photographer come to our business<br>brought back memories of school photos.<br>But Marcus made it all very relaxed and easy and readily put us all at ease<br>knowing our faces were in good hands.</p>
    <p class="testimonial__sign">Daniel Porter</p>
    <p class="testimonial__org">Veltrix</p>
  </blockquote>

  <span class="client" style="left:85px"><span class="client__dot"></span>Goldarch</span>
  <span class="client" style="left:175px">Brightmart</span>
  <span class="client" style="left:313px">Cellar Row</span>
  <span class="client" style="left:460px">Stridelane</span>
  <div class="abs review">
    <p class="review__name">Marcus Ellery Photography</p>
    <p class="review__addr">12 Harbour Lane, Northbridge</p>
    <p class="review__score">5.0 <span class="review__stars">★★★★★</span> <span class="review__count">90 reviews</span></p>
  </div>
</section>

</body>
</html>
```